Ravelor Global Kft. is an online recruitment marketplace connecting the employers and recruiters together. We provide an e-bussiness solution for companies and give busines opportunity for recruiters.
We have a logo design already, which should be used on the business card.
Our colours are grey and magenta, which can be seen in the logo. Black is also welcome.
The style should be dynamic, young but professional. It should be clear, visible, elegant, not too crowded, simple but exciting.
We need the following data on the BC: name, title, address, phone,fax and mobile number, email address, website.
Target Market(s)
Our target market are companies, as this is a B2B business. We also target recruiters, recruitment professionals, headhunters.We would like to be impressive and different.
Industry/Entity Type
Business
Requirements
Must have
- We would like to promote our website, www.ravelorglb.hu.
- Please, put this on the back with a quite visible letter size.The style should be dynamic, young but professional. It should be clear, visible, elegant, not too crowded, simple but exciting.
Should not have
- We do not want to see people figures.

```html
<!DOCTYPE html>
<html lang="en">
<head>
<meta charset="utf-8">
<title>Ravelor Global Kft. – Business Card</title>
<link href="https://fonts.googleapis.com/css2?family=Arimo:wght@400;700&display=swap" rel="stylesheet">
<style>
  :root {
    --stage: #000000;
    --card: #ffffff;
    --magenta: #e5097f;
    --grey: #8c8c8c;
    --ink: #333333;
    --band-dark: #3a3a3a;
    --band-mid: #6e6e6e;
    --stripe: #cfcfcf;
  }
  * { margin: 0; padding: 0; box-sizing: border-box; }
  html, body {
    width: 1200px; height: 900px; overflow: hidden;
    background: var(--stage);
    font-family: "Arimo", Arial, sans-serif;
  }
  .card {
    position: absolute; top: 306px;
    width: 504px; height: 290px;
    background: var(--card);
    border-radius: 20px;
    overflow: hidden;
  }
  .card--front { left: 80px; }
  .card--back { left: 618px; }
  .card__band { position: absolute; left: 0; top: 0; width: 504px; height: 290px; }

  .contact { position: absolute; left: 26px; top: 54px; color: var(--ink); }
  .contact__name { color: var(--magenta); font-weight: 700; font-size: 16px; }
  .contact__title { font-size: 11px; margin-top: 4px; }
  .contact__address { font-size: 11px; line-height: 18px; margin-top: 20px; }
  .contact__lines { list-style: none; margin-top: 12px; font-size: 11px; }
  .contact__lines li { display: flex; align-items: center; height: 18px; }
  .contact__lines svg { width: 12px; height: 12px; margin-right: 8px; fill: var(--ink); }
  .contact__lines .contact__email { margin-top: 16px; }

  .brand { position: absolute; display: flex; align-items: center; }
  .brand__mark { background: var(--grey); flex: none; }
  .brand__name { color: var(--magenta); font-weight: 700; letter-spacing: 0.5px; white-space: nowrap; }
  .card--front .brand { left: 266px; top: 88px; }
  .card--front .brand__mark { width: 38px; height: 38px; margin-right: 10px; }
  .card--front .brand__name { font-size: 30px; }
  .card--back .brand { left: 118px; top: 88px; }
  .card--back .brand__mark { width: 60px; height: 60px; margin-right: 14px; }
  .card--back .brand__name { font-size: 46px; }

  .website {
    position: absolute; left: 18px; top: 242px;
    color: #ffffff; font-size: 15px; font-weight: 700; letter-spacing: 3px;
    white-space: nowrap;
  }
</style>
</head>
<body>
  <section class="card card--front" aria-label="Business card front">
    <svg class="card__band" viewBox="0 0 504 290" aria-hidden="true">
      <defs>
        <linearGradient id="bandFront" x1="0" y1="0" x2="0" y2="1">
          <stop offset="0" stop-color="var(--band-mid)"/>
          <stop offset="1" stop-color="var(--band-dark)"/>
        </linearGradient>
      </defs>
      <path d="M0 252 L255 252 C285 252 290 218 325 218 L504 218 L504 290 L0 290 Z" fill="var(--stripe)"/>
      <path d="M0 258 L258 258 C288 258 292 224 326 224 L504 224 L504 290 L0 290 Z" fill="url(#bandFront)"/>
    </svg>

    <div class="contact">
      <p class="contact__name">Mara Vell</p>
      <p class="contact__title">President</p>
      <p class="contact__address">Level 4, 12 - 18 Ostrava<br>St Elmwood Park NSW 2099</p>
      <ul class="contact__lines">
        <li><svg viewBox="0 0 12 12"><path d="M1 4 Q6 0 11 4 L10 6 L8 5 L8 4 Q6 3 4 4 L4 5 L2 6 Z M3 7 H9 L10 11 H2 Z"/></svg>1300 555 174</li>
        <li><svg viewBox="0 0 12 12"><rect x="3.5" y="0.5" width="5" height="11" rx="1"/></svg>02 9555 0187</li>
        <li><svg viewBox="0 0 12 12"><path d="M3 1 H9 V5 H3 Z M1 5 H11 V11 H1 Z"/></svg>02 9555 0187</li>
        <li class="contact__email"><svg viewBox="0 0 12 12"><path d="M0.5 2 H11.5 V10 H0.5 Z M1.5 3 L6 6.5 L10.5 3" fill="none" stroke="var(--ink)" stroke-width="1.2"/></svg>info@ravelorglb.com</li>
      </ul>
    </div>

    <div class="brand">
      <span class="brand__mark"></span>
      <span class="brand__name">RAVELOR</span>
    </div>
  </section>

  <section class="card card--back" aria-label="Business card back">
    <svg class="card__band" viewBox="0 0 504 290" aria-hidden="true">
      <defs>
        <linearGradient id="bandBack" x1="0" y1="0" x2="0" y2="1">
          <stop offset="0" stop-color="var(--band-mid)"/>
          <stop offset="1" stop-color="var(--band-dark)"/>
        </linearGradient>
      </defs>
      <path d="M0 218 L188 218 C223 218 228 252 258 252 L504 252 L504 290 L0 290 Z" fill="var(--stripe)"/>
      <path d="M0 224 L186 224 C220 224 224 258 256 258 L504 258 L504 290 L0 290 Z" fill="url(#bandBack)"/>
    </svg>

    <div class="brand">
      <span class="brand__mark"></span>
      <span class="brand__name">RAVELOR</span>
    </div>

    <p class="website">www.ravelorglb.hu</p>
  </section>
</body>
</html>
```